VeltaFilez Website

VeltaFiles - Sorted Case Records
We need a Web design for a new company called - VeltaFilez.
VeltaFilez is a Personal Injury and Medical Record Legal Service Outsourcing company. We help Personal Injury Attorneys - with fact based Medical Chronologies and Summaries.

We take Medical Records in disarray and put them in order and summarize them in a chronological order and Update them as needed (if more medical records are added)
Take Releases (for medical records) and work with doctor practices and get the records if needed

Target Market(s)

Personal Injury Attorneys

Industry/Entity Type

Attorney

Number of Pages Required

2 page

Font styles to use
Serif
Sans Serif

Colors

Designer to choose colors to be used in the design.

Requirements
Must have
• Professional Design
• Just need the design for the Home page and Internal pages - I will do the Coding for the pages in html and/or wordpress.
• Don't worry about the content - just need a design.

```html
<!DOCTYPE html>
<html lang="en">
<head>
<meta charset="utf-8">
<title>VeltaFilez – Sorted Case Records</title>
<link rel="stylesheet" href="https://fonts.googleapis.com/css2?family=Arimo:wght@400;700&display=swap">
<style>
  :root {
    --canvas: #cbcbcb;
    --page: #ffffff;
    --green: #b2c86e;
    --navy: #1d3f7c;
    --ink: #3a3a3a;
    --muted: #5a5a5a;
    --panel: #c9c9c9;
    --icon: #8c8c8c;
  }
  * { box-sizing: border-box; margin: 0; padding: 0; }
  html, body { width: 1200px; height: 1200px; overflow: hidden; background: var(--canvas); }
  body { font-family: "Arimo", Arial, sans-serif; position: relative; }
  .page { position: absolute; left: 90px; top: 0; width: 1002px; height: 1200px; background: var(--page); }
  .abs { position: absolute; }

  .topbar { left: 0; top: 0; width: 1002px; height: 29px; background: var(--green); }
  .social { display: flex; gap: 5px; left: 168px; top: 4px; }
  .social span { width: 20px; height: 20px; background: var(--icon); display: block; }
  .hotline { right: 142px; top: 8px; color: #fff; font-weight: 700; font-size: 12px; }

  .brand { left: 169px; top: 50px; color: var(--navy); }
  .brand-name { display: flex; align-items: center; gap: 6px; font-size: 20px; font-weight: 700; }
  .brand-name i { width: 14px; height: 14px; background: var(--navy); display: block; }
  .brand-tag { font-size: 8px; color: #222; margin-top: 3px; }

  .nav { top: 81px; font-size: 12px; color: var(--navy); }

  .hero { left: 169px; top: 120px; width: 695px; height: 359px;
    background: linear-gradient(100deg, #6f6f6f 0%, #9a9a92 18%, #e4e6e4 38%, #eef0ef 55%, #9fb8d8 75%, #e9ecee 100%); }

  .intro { left: 169px; top: 507px; width: 341px; color: var(--navy); font-size: 11px; line-height: 12.7px; font-weight: 700; }
  .intro p + p { margin-top: 12.7px; }

  .section-title { display: flex; align-items: flex-end; gap: 4px; color: var(--navy); font-size: 14px; font-weight: 400; }
  .section-title::after { content: ""; flex: 1; height: 2px; background: var(--green); margin-bottom: 3px; }

  .services-title { left: 539px; top: 506px; width: 325px; }
  .service-card { top: 525px; width: 155px; height: 132px; background: var(--green); }
  .read-more { top: 672px; width: 74px; height: 18px; background: var(--green); color: #fff; font-size: 11px; font-weight: 700; line-height: 18px; padding-left: 7px; }

  .clients-title { left: 169px; top: 802px; width: 695px; }
  .testimonial { top: 838px; width: 215px; }
  .quote { height: 47px; background: var(--panel); color: var(--muted); font-size: 9.5px; line-height: 12px; padding: 15px 19px 0; }
  .client-name { text-align: center; margin-top: 7px; font-size: 9.5px; font-weight: 700; color: var(--ink); }
  .client-date { text-align: center; margin-top: 3px; font-size: 7px; color: var(--green); }

  .list-title { left: 169px; top: 935px; color: var(--navy); font-size: 14px; font-weight: 400; }
  .logo-strip { left: 169px; top: 958px; width: 695px; height: 88px; background: var(--panel); overflow: hidden; }
  .logo-tile { top: 12px; width: 117px; height: 63px; background: #fff; display: flex; flex-direction: column; align-items: center; justify-content: center; color: var(--navy); }
  .logo-tile b { font-size: 13px; display: flex; align-items: center; gap: 4px; }
  .logo-tile b i { width: 9px; height: 9px; background: var(--navy); display: block; }
  .logo-tile small { font-size: 6px; color: #222; margin-top: 2px; }

  .divider { left: 169px; top: 1069px; width: 695px; height: 2px; background: var(--green); }

  .address { left: 169px; top: 1097px; color: var(--muted); font-size: 9.5px; line-height: 11.5px; font-weight: 700; }
  .address h4 { font-size: 9.5px; margin-bottom: 11px; }
  .feed { top: 1097px; width: 220px; font-size: 8px; line-height: 10px; color: var(--muted); }
  .feed h4 { color: var(--navy); font-size: 9px; margin-bottom: 8px; }
  .feed time { display: block; color: var(--navy); font-size: 7px; margin-top: 2px; }

  .footer-bar { left: 169px; top: 1184px; width: 695px; height: 16px; background: var(--green); color: #fff; font-size: 7px; text-align: center; line-height: 16px; }
</style>
</head>
<body>
<div class="page">
  <header>
    <div class="abs topbar"></div>
    <div class="abs social" aria-label="Social links"><span></span><span></span><span></span></div>
    <div class="abs hotline">Hotline number - 0022 - 456 - 7890</div>

    <div class="abs brand">
      <div class="brand-name"><i></i>VELTAFILEZ</div>
      <div class="brand-tag">Sorted Case Records</div>
    </div>
    <nav>
      <span class="abs nav" style="left:481px">Link 01</span>
      <span class="abs nav" style="left:570px">Link 02</span>
      <span class="abs nav" style="left:653px">Link 03</span>
      <span class="abs nav" style="left:734px">Link 04</span>
      <span class="abs nav" style="left:822px">Link 05</span>
    </nav>
  </header>

  <div class="abs hero" role="img" aria-label="Photo of a consultant with a clipboard talking with a client seated on a sofa"></div>

  <section class="abs intro">
    <p>Lorem ipsum dolor sit amet, consectetur adipiscing elit, sed do eiusmod tempor incididunt ut labore et dolore magna aliqua. Ut aliquam purus sit amet. Dictum sit amet justo donec. Magnis dis parturient montes nascetur ridiculus mus mauris vitae. Nunc non blandit massa enim nec dui nunc mattis enim. Scelerisque felis imperdiet proin fermentum leo vel orci porta. Turpis egestas integer eget aliquet nibh. Mauris vitae ultricies leo integer malesuada nunc vel. Blandit turpis cursus in hac habitasse platea dictumst. Velit ut tortor pretium viverra suspendisse.</p>
    <p>Elementum nibh tellus molestie nunc non blandit massa enim. Tincidunt ornare massa eget egestas purus viverra. Eget dolor morbi non arcu risus. Quis hendrerit dolor magna eget est lorem ipsum. Risus commodo viverra maecenas accumsan lacus. Dui sapien eget mi proin sed. Commodo nulla facilisi nullam vehicula ipsum a arcu cursus vitae. Sed elementum tempus egestas sed sed risus pretium. Amet mattis vulputate enim nulla. Sapien nec sagittis aliquam malesuada bibendum arcu. Massa vitae tortor condimentum lacinia quis vel. Semper viverra nam libero justo laoreet sit amet cursus sit. Sit amet mauris commodo quis imperdiet. Tempus iaculis urna id volutpat.</p>
  </section>

  <section>
    <h2 class="abs section-title services-title">Services</h2>
    <div class="abs service-card" style="left:539px"></div>
    <div class="abs service-card" style="left:708px"></div>
    <div class="abs read-more" style="left:539px">Read More</div>
    <div class="abs read-more" style="left:708px">Read More</div>
  </section>

  <section>
    <h2 class="abs section-title clients-title">What our clients say</h2>
    <div class="abs testimonial" style="left:169px">
      <div class="quote">"Absolutely fantastic job – very detailed and thorough."</div>
      <div class="client-name">Client Name</div>
      <div class="client-date">DD/MM/YYYY | MONDAY</div>
    </div>
    <div class="abs testimonial" style="left:410px">
      <div class="quote">"Absolutely fantastic job – very detailed and thorough."</div>
      <div class="client-name">Client Name</div>
      <div class="client-date">DD/MM/YYYY | MONDAY</div>
    </div>
    <div class="abs testimonial" style="left:648px">
      <div class="quote">"Absolutely fantastic job – very detailed and thorough."</div>
      <div class="client-name">Client Name</div>
      <div class="client-date">DD/MM/YYYY | MONDAY</div>
    </div>
  </section>

  <section>
    <h2 class="abs list-title">List of clients</h2>
    <div class="abs logo-strip">
      <div class="abs logo-tile" style="left:-98px"><b><i></i>VELTAFILEZ</b><small>Sorted Case Records</small></div>
      <div class="abs logo-tile" style="left:48px"><b><i></i>VELTAFILEZ</b><small>Sorted Case Records</small></div>
      <div class="abs logo-tile" style="left:193px"><b><i></i>VELTAFILEZ</b><small>Sorted Case Records</small></div>
      <div class="abs logo-tile" style="left:338px"><b><i></i>VELTAFILEZ</b><small>Sorted Case Records</small></div>
      <div class="abs logo-tile" style="left:487px"><b><i></i>VELTAFILEZ</b><small>Sorted Case Records</small></div>
      <div class="abs logo-tile" style="left:636px"><b><i></i>VELTAFILEZ</b><small>Sorted Case Records</small></div>
    </div>
  </section>

  <footer>
    <div class="abs divider"></div>
    <div class="abs address">
      <h4>ADDRESS -</h4>
      VELTAFILEZ<br>Sorted Case Records<br>Line 01<br>Line 02<br>Line 03
    </div>
    <div class="abs feed" style="left:367px">
      <h4>Latest Tweets</h4>
      Lorem ipsum dolor sit amet, consectetur adipiscing elit, sed do eiusmod tempor incididunt ut labore et dolore magna aliqua.
      <time>February 24, 2018 11.00 am</time>
    </div>
    <div class="abs feed" style="left:648px">
      <h4>Latest Updates</h4>
      Lorem ipsum dolor sit amet, consectetur adipiscing elit, sed do eiusmod tempor incididunt ut labore et dolore magna aliqua.
      <time>February 24, 2018 11.00 am</time>
    </div>
    <div class="abs footer-bar">Legal disclaimer | Privacy Policy | Copyright © 2018 veltafilez.</div>
  </footer>
</div>
</body>
</html>
```